Design a Bold Tradeshow Backdrop for a Sustainable Cleaning Technology

We need a professional, high-impact 10' × 8' tradeshow backdrop for Veldrix®, a commercial cleaning technology company. 143.75" x 90" high and needs bleeds in the 143.75" direction for printing but the graphic area is 10' wide.

Our first event will have an audience that includes K–12 school administrators, facility managers, business officials, and custodial decision-makers. However, this backdrop will be used at multiple future trade shows across different commercial and institutional markets.

The design therefore needs to be universal rather than specifically education- or school-themed.

Our goal is to stop attendees as they walk past the booth and immediately communicate a simple message:

Safer and more sustainable cleaning can also cost substantially less than conventional cleaning chemicals.

We want the design to feel modern, innovative, clean, sustainable, credible, commercial, and premium. It should resonate with K–12 decision-makers while being equally appropriate at events serving commercial facilities, healthcare, hospitality, government, property management, transportation, and other institutional markets.

It should NOT look like a traditional janitorial supply advertisement and should not be overly busy.

The most important messages need to be understandable from approximately 10–20 feet away.

Required Messaging

The primary headline should be:

SUSTAINABLE CLEANING
DOES NOT HAVE TO BE EXPENSIVE.

Three major value propositions should be prominently displayed:

FREE
Cleaning Chemical Analysis
See how much you can save.

SAVE UP TO 60% or More
on Cleaning Chemical Costs

AS LITTLE AS $0.27/GALLON

We would also like a strong secondary message incorporated into the design:

SMARTER CLEANING.
High Performance. Low Cost. Safer.

Visual Direction — Important

Rather than showing a K–12 school hallway or other environment that limits the backdrop to the education market, we want a sophisticated, universal commercial or institutional environment.

This could be a bright, contemporary commercial facility, lobby, corridor, office environment, public building, or other premium architectural space that could reasonably represent many different types of facilities.

The environment should communicate:

Cleanliness • Safety • Sustainability • Professionalism • Efficiency • High Performance

We want someone from a school, hospital, hotel, office building, airport, government facility, or other commercial property to be able to look at the backdrop and relate the imagery to their own facility.

Please avoid imagery that makes the backdrop industry-specific.

We also want to avoid clichéd environmental imagery. The design does not need to be covered in leaves, trees, water droplets, recycling symbols, or other obvious "green" graphics to communicate sustainability. We prefer a sophisticated commercial interpretation of sustainability.

Color & Brand Direction

We want the overall color palette to stay primarily within:

Blues — consistent with our corporate identity

Greens — to reinforce sustainability, safety, efficiency, and environmental responsibility

White — strongly encouraged for clean space, contrast, and an open contemporary appearance

Black — should be limited primarily to text where necessary for readability

Please avoid making black a major background or dominant design color.

We want the finished display to have a bright, clean, sophisticated, sustainable look and feel rather than a dark or industrial appearance.

The design should use significant negative space and a strong visual hierarchy.

Less is more.

We prefer a few large, powerful messages that can be understood quickly rather than numerous small bullet points, paragraphs, or icons.

Creative Freedom

The attached concept image is provided to communicate our general direction and messaging only.

It does not need to be copied.

We are specifically running this contest because we want designers to improve upon our initial concept and show us different creative approaches to presenting the Veldrix value proposition.

We are open to creative interpretations of the commercial environment, composition, typography, use of negative space, and how the three major financial benefits are presented.

The finished design should feel like an innovative commercial technology brand, not simply another cleaning chemical company.

Corporate Logo — Very Important

We are attaching our official Veldrix® corporate logo for use in the design.

DO NOT redraw, recreate, modify, stylize, reinterpret, trace, or AI-generate the Veldrix logo.

The supplied corporate logo must be inserted directly into the artwork exactly as provided, maintaining its original proportions, colors, typography, trademark elements, and graphic design.

The logo should generally appear in the upper-left area of the backdrop but should not overwhelm the primary marketing message.

Printer Template & Graphic Sizing

We are also attaching the printer's official graphic template and instructions for the 8' × 8' tension-fabric display.

Designers should create their artwork using these supplied specifications so the winning design can be transferred directly into production.

The printer requires that the original document size not be changed, artwork be created on the designated design layer or a new layer, images be embedded, text be converted to outlines, and the finished production artwork be supplied as a PDF.

Please pay particular attention to the bleed area, finished size, and safe artwork area when positioning important text, graphics, and the corporate logo.

Physical Booth Context

The backdrop will sit behind an 8' tradeshow table.

The complete booth will also contain:

A blue stretch tablecloth with the Veldrix corporate logo
Morvaqs and Veldrix product containers and samples on the table
An Lunadrav chemical mixing/dilution station displayed on an elevated stand to the left
A television/monitor to the right demonstrating our online ROI cost-savings calculator

Because these other booth elements will explain our products and technology in greater detail, the backdrop should NOT attempt to explain everything we do.

Its primary purpose is to stop traffic, establish the Veldrix brand, and communicate our core economic and sustainability value proposition.

Final Deliverables

The winning designer must provide artwork properly sized and positioned using our supplied 8' × 8' tension-fabric display template.

Final files should include:

Print-ready, high-resolution PDF
Editable source/vector artwork
All images embedded
Fonts converted to outlines
Artwork correctly positioned within the supplied printer template
Original Veldrix corporate logo incorporated without modification
The 3–5 Second Test

This is perhaps the most important requirement.

Someone walking down a tradeshow aisle should be able to look at the backdrop for 3–5 seconds and understand:

Veldrix offers safer, sustainable, high-performance commercial cleaning — at a lower cost.

The three offers we particularly want them to remember are:

FREE CHEMICAL ANALYSIS

SAVE UP TO 60%

AS LITTLE AS $0.27/GALLON

The overall takeaway should be:

Sustainable cleaning does not have to cost more.

We want the winning design to make that message immediately understandable, credible, and memorable.

Colors
0054AA
0677BA
7BADD7
CADEEF
E8F1F8
0094D4
00A9DD
6FCCEA
C7EBF8
E9F6FB
00AB8E
00BBA5
67D7C9
C6EFE9
E9F9F6
59FF00
82FF00
B8FF75
E3FFCB
F4FFEA

```html
<!DOCTYPE html>
<html lang="en">
<head>
<meta charset="utf-8">
<title>Veldrix Tradeshow Backdrop</title>
<link rel="stylesheet" href="https://fonts.googleapis.com/css2?family=Montserrat:wght@500;600;800;900&family=Lexend:wght@400;600&display=swap">
<style>
  :root{
    --page:#adadbb;
    --white:#ffffff;
    --blue-deep:#1b3c80;
    --blue:#0054AA;
    --blue-mid:#0677BA;
    --green:#7cc142;
    --ink:#1a1a1a;
    --photo-a:#dfe6ea;
    --photo-b:#f3f6f7;
  }
  *{margin:0;padding:0;box-sizing:border-box}
  html,body{width:763px;height:1200px;overflow:hidden}
  body{background:var(--page);position:relative;font-family:"Montserrat",sans-serif}

  .backdrop{position:absolute;left:31px;top:250px;width:700px;height:700px;background:var(--white);overflow:hidden;box-shadow:0 6px 14px rgba(0,0,0,.25)}

  .scene-photo{position:absolute;left:90px;top:100px;width:610px;height:600px;
    background:
      linear-gradient(to bottom,rgba(255,255,255,0) 70%,#fff 100%),
      linear-gradient(to right,#fff 0%,rgba(255,255,255,0) 30%),
      radial-gradient(ellipse at 70% 55%,#c9d2d8 0%,var(--photo-a) 40%,var(--photo-b) 75%)}

  .decor{position:absolute;left:0;top:0;width:700px;height:700px}

  .brand{position:absolute;left:25px;top:26px;display:flex;align-items:center;gap:8px}
  .brand-square{width:22px;height:22px;background:#f4c20d}
  .brand-name{font-family:"Lexend",sans-serif;font-weight:600;font-size:28px;color:var(--ink);letter-spacing:-.5px}

  .headline{position:absolute;left:25px;top:126px;font-weight:900;line-height:1;color:var(--blue)}
  .headline span{display:block}
  .hl-1{font-size:36px;letter-spacing:-.6px}
  .hl-2{font-size:49px;color:var(--green);letter-spacing:-.5px;margin-top:1px}
  .hl-3{font-size:19px;font-weight:800;margin-top:3px;letter-spacing:-.3px}
  .hl-4{font-size:36px;margin-top:2px;letter-spacing:-.8px}

  .offers{position:absolute;left:26px;top:285px;width:232px;height:282px;border-radius:15px;
    background:linear-gradient(135deg,var(--blue-deep) 0%,var(--blue) 100%);color:var(--white)}
  .offer-icon{position:absolute;left:15px;width:44px;height:46px}
  .offer-text{position:absolute;left:73px;line-height:1}
  .divider{position:absolute;left:15px;width:200px;height:2px;background:linear-gradient(to right,var(--green),rgba(124,193,66,.15))}
  .big{font-weight:900;color:var(--green);letter-spacing:-.8px;display:block}
  .label{font-weight:500;font-size:14px;letter-spacing:-.6px;display:block}
  .fine{font-weight:500;font-size:8px;letter-spacing:-.2px;display:block}

  .tagline{position:absolute;left:475px;top:28px;color:var(--white)}
  .tag-1,.tag-2{display:block;font-weight:800;font-size:28px;line-height:.92;letter-spacing:-.3px}
  .tag-2{color:var(--green)}
  .tag-rule{display:block;width:54px;height:3px;margin:9px 0 7px;background:linear-gradient(to right,var(--green),var(--blue-mid))}
  .tag-lines{font-family:"Lexend",sans-serif;font-weight:400;font-size:21.5px;line-height:.96;letter-spacing:-.2px}
</style>
</head>
<body>
<main class="backdrop">
  <div class="scene-photo" role="img" aria-label="Photo of two cleaning staff in aprons and red gloves wiping a counter in a bright modern office"></div>

  <svg class="decor" viewBox="0 0 700 700" aria-hidden="true">
    <defs>
      <linearGradient id="arc-grad" x1="0" y1="0" x2="0" y2="1">
        <stop offset="0" stop-color="#7cc142"/>
        <stop offset=".45" stop-color="#3f9a88"/>
        <stop offset="1" stop-color="#0054AA"/>
      </linearGradient>
      <linearGradient id="disc-grad" x1="0" y1="0" x2="1" y2="0">
        <stop offset="0" stop-color="#1b3c80"/>
        <stop offset="1" stop-color="#0054AA"/>
      </linearGradient>
    </defs>
    <path d="M437 -5 C 434 190, 340 350, 200 385 C 120 402, 40 405, -5 405" fill="none" stroke="url(#arc-grad)" stroke-width="13"/>
    <path d="M444 0 C 438 60, 428 115, 442 152 C 466 182, 520 190, 575 188 C 630 186, 672 168, 700 140 V 0 Z" fill="url(#disc-grad)"/>
  </svg>

  <div class="brand">
    <span class="brand-square"></span>
    <span class="brand-name">Veldrix®</span>
  </div>

  <h1 class="headline">
    <span class="hl-1">SUSTAINABLE</span>
    <span class="hl-2">CLEANING</span>
    <span class="hl-3">DOES NOT HAVE TO</span>
    <span class="hl-4">BE EXPENSIVE.</span>
  </h1>

  <section class="offers">
    <svg class="offer-icon" style="top:24px" viewBox="0 0 44 46" aria-hidden="true">
      <path d="M40 14 V3 H3 V43 H40 V32" fill="none" stroke="#fff" stroke-width="3"/>
      <path d="M18 12 H26 M19.5 12 V20 L13 33 H31 L24.5 20 V12" fill="none" stroke="#7cc142" stroke-width="1.8" stroke-linejoin="round"/>
      <circle cx="19" cy="29" r="1.4" fill="#7cc142"/><circle cx="24" cy="27" r="1.1" fill="#7cc142"/>
    </svg>
    <div class="offer-text" style="top:20px">
      <span class="big" style="font-size:37px">FREE</span>
      <span class="label" style="margin-top:2px">CHEMICAL ANALYSIS</span>
      <span class="fine" style="margin-top:1px">See how much you can save.</span>
    </div>
    <div class="divider" style="top:95px"></div>

    <svg class="offer-icon" style="top:119px" viewBox="0 0 44 46" aria-hidden="true">
      <path d="M40 14 V3 H3 V43 H40 V32" fill="none" stroke="#fff" stroke-width="3"/>
      <path d="M13 33 C 13 20, 22 13, 31 12 C 31 24, 24 32, 13 33 Z M13 33 L 25 19" fill="none" stroke="#7cc142" stroke-width="1.8" stroke-linejoin="round"/>
    </svg>
    <div class="offer-text" style="top:114px">
      <span class="label">SAVE UP TO</span>
      <span class="big" style="font-size:35px;margin-top:1px">60%</span>
      <span class="fine" style="margin-top:1px">on Cleaning Chemical Costs</span>
    </div>
    <div class="divider" style="top:187px"></div>

    <svg class="offer-icon" style="top:211px" viewBox="0 0 44 46" aria-hidden="true">
      <path d="M40 14 V3 H3 V43 H40 V32" fill="none" stroke="#fff" stroke-width="3"/>
      <path d="M27 16 C 25 13.5, 16 13.5, 16 18.5 C 16 23.5, 28 21.5, 28 27 C 28 32, 18 32, 16 29 M22 10 V35" fill="none" stroke="#7cc142" stroke-width="1.8" stroke-linecap="round"/>
    </svg>
    <div class="offer-text" style="top:204px">
      <span class="label">AS LITTLE AS</span>
      <span class="big" style="font-size:36px">$0.27</span>
      <span class="label" style="font-size:15px;margin-top:1px">/ GALLON</span>
    </div>
  </section>

  <div class="tagline">
    <span class="tag-1">SMARTER</span>
    <span class="tag-2">CLEANING.</span>
    <span class="tag-rule"></span>
    <p class="tag-lines">High Performance.<br>Low Cost.<br>Safer.</p>
  </div>
</main>
</body>
</html>
```